Bramble Bites Society - A Monthly Subscription Dog Treats Club - Shopify Website Design

A monthly subscription company. Need a Shopify Website Design and uploaded to fully work with Tidewell Recurring.

Please look at these sites for examples as well as the images I enclosed.

https://www.platemarlo.example/
https://www.quirktastebox.example/

Number of Pages Required

1 page

```html
<!DOCTYPE html>
<html lang="en">
<head>
<meta charset="utf-8">
<title>Bramble Bites Society – Monthly Dog Treats Club</title>
<link href="https://fonts.googleapis.com/css2?family=Arimo:wght@400;700&family=Montserrat:wght@400&display=swap" rel="stylesheet">
<style>
:root{
  --tan:#cc9364;
  --tan-light:#d29c6e;
  --ink:#2b2b2b;
  --muted:#666;
  --line:#d8d8d8;
  --footer:#000;
  --white:#fff;
}
*{box-sizing:border-box;margin:0;padding:0}
html,body{width:1200px;height:3327px;overflow:hidden;background:var(--white)}
body{position:relative;font-family:"Arimo",Arial,sans-serif;color:var(--ink)}
.abs{position:absolute}
a{color:inherit;text-decoration:none}

/* header */
.utility{top:14px;font-size:12px;font-weight:700;display:flex;align-items:center;gap:4px}
.utility svg{width:12px;height:12px}
.utility-search{left:111px}
.utility-cart{right:111px}
.brand{left:111px;top:55px;font-size:22px;font-weight:700;color:var(--tan);letter-spacing:.3px}
.nav{right:111px;top:58px;display:flex;gap:34px;font-size:14px}
.nav a{position:relative;padding-bottom:12px}
.nav .active{color:var(--tan)}
.nav .active::after{content:"";position:absolute;left:-5px;right:-5px;bottom:0;height:3px;background:var(--tan)}

/* hero */
.hero-photo{left:560px;top:110px;width:640px;height:562px;background:radial-gradient(ellipse at 55% 55%,#d8c1a6 0%,#ece3d8 45%,#fbfaf8 80%)}
.hero-title{left:97px;top:250px;font-size:54px;font-weight:700;color:var(--tan-light);letter-spacing:.5px}
.hero-sub{left:97px;top:320px;font-size:14px}
.btn{display:flex;align-items:center;justify-content:center;background:var(--tan);color:var(--white);font-size:14px;font-weight:700;letter-spacing:.3px}
.hero-btn{left:97px;top:357px;width:146px;height:47px}

/* feature grid */
.photo{position:absolute}
.feature-title{font-size:21px;font-weight:700;letter-spacing:.3px}
.feature-text{font-size:13px;line-height:26px;color:var(--muted);width:480px}

/* banner */
.banner{left:0;top:1580px;width:1200px;height:397px;background:linear-gradient(135deg,#b89c74 0%,#8a7558 40%,#3a3430 60%,#9d8866 80%,#c4ab80 100%)}
.banner-title{left:0;width:1200px;top:1715px;text-align:center;font-size:36px;font-weight:700;color:var(--white);letter-spacing:.4px}
.banner-btn{left:528px;top:1771px;width:146px;height:48px}

/* arrivals */
.section-title{left:0;width:1200px;text-align:center;font-size:35px;font-weight:700;letter-spacing:.3px}
.product{top:2108px;width:233px;height:340px;border:1px solid var(--line)}
.product-photo{position:absolute;left:10px;top:10px;width:211px;height:170px}
.product-name{position:absolute;left:26px;top:197px;font-size:19px}
.product-price{position:absolute;left:26px;top:233px;font-size:18px}
.product-btn{position:absolute;left:26px;top:267px;width:146px;height:49px}

/* how it works */
.step{top:2597px;width:314px;height:225px;display:flex;align-items:center;justify-content:center;color:var(--white);font-size:18px;font-weight:700}

/* promo */
.promo{left:0;top:2917px;width:1200px;height:75px;background:var(--tan);color:var(--white);font-size:17px;font-weight:700;display:flex;align-items:center;justify-content:center}

/* footer */
.footer{left:0;top:2992px;width:1200px;height:335px;background:var(--footer);color:var(--white)}
.footer-col{position:absolute;top:70px}
.footer-col h3{font-size:20px;font-weight:700;margin-bottom:14px}
.footer-col p,.footer-col li{font-size:13px;line-height:26px;list-style:none}
.email{position:absolute;left:806px;top:131px;width:283px;height:43px;background:#3a3a3a;color:#bbb;font-size:13px;padding:14px 16px}
.join{position:absolute;left:807px;top:182px;width:110px;height:43px}
.copyright{position:absolute;left:111px;top:270px;font-family:"Montserrat",Arial,sans-serif;font-size:14px}
.payments{position:absolute;right:111px;top:265px;display:flex;gap:8px}
.payments span{width:40px;height:26px;background:#1f3e8f;color:var(--white);font-size:8px;font-weight:700;display:flex;align-items:center;justify-content:center;border-radius:3px}
</style>
</head>
<body>

<header>
  <div class="abs utility utility-search"><svg viewBox="0 0 12 12" aria-hidden="true"><circle cx="5" cy="5" r="3.5" fill="none" stroke="#000" stroke-width="1.6"/><line x1="7.5" y1="7.5" x2="11" y2="11" stroke="#000" stroke-width="1.8"/></svg>Search</div>
  <div class="abs utility utility-cart"><svg viewBox="0 0 12 12" aria-hidden="true"><path d="M0 1h2l2 7h6l2-5H3" fill="none" stroke="#000" stroke-width="1.4"/><circle cx="5" cy="10.5" r="1" fill="#000"/><circle cx="9" cy="10.5" r="1" fill="#000"/></svg>Cart 0</div>
  <div class="abs brand">BRAMBLE BITES SOCIETY</div>
  <nav class="abs nav">
    <a class="active" href="#">Home</a><a href="#">About</a><a href="#">product</a><a href="#">Blog</a><a href="#">Review</a><a href="#">Contact us</a>
  </nav>
</header>

<section class="hero">
  <div class="abs hero-photo" role="img" aria-label="Puppy eating bone-shaped biscuits from a cardboard box"></div>
  <h1 class="abs hero-title">BRAMBLE BITES SOCIETY</h1>
  <p class="abs hero-sub">Nemo enim ipsam voluptatem quia voluptas sit</p>
  <a class="abs btn hero-btn" href="#">SHOP NOW</a>
</section>

<section class="features">
  <div class="photo" style="left:111px;top:690px;width:481px;height:391px;background:linear-gradient(160deg,#c8c8c8 0%,#b9a58a 45%,#b32a2e 85%)" role="img" aria-label="Red gift box full of heart and bone biscuits"></div>
  <div class="photo" style="left:608px;top:690px;width:481px;height:236px;background:linear-gradient(120deg,#5b5a55 0%,#b0683a 45%,#d9d3cc 100%)" role="img" aria-label="Spaniel resting beside a treat tin"></div>
  <h2 class="abs feature-title" style="left:610px;top:945px">BRAMBLE BITES SOCIETY</h2>
  <p class="abs feature-text" style="left:611px;top:982px">Lorem ipsum dolor sit amet, consectetur adipiscing elit, sed do eiusmod tem por incididunt ut labore et dolore magna Lorem ipsum dolor sit amet, conse ctetur adipiscing elit, sed do eiusmod tempor incididunt ut labore</p>

  <div class="photo" style="left:111px;top:1102px;width:481px;height:322px;background:radial-gradient(ellipse at 55% 50%,#b32a2a 0%,#7a4a2a 45%,#5c3a22 100%)" role="img" aria-label="Measuring cup lying in dry dog food"></div>
  <h2 class="abs feature-title" style="left:111px;top:1444px">WHAT'S IN A BOX?</h2>
  <p class="abs feature-text" style="left:112px;top:1481px">Lorem ipsum dolor sit amet, consectetur adipiscing elit, sed do eiusmod tem por incididunt ut labore et dolore magna Lorem ipsum dolor sit amet, conse ctetur adipiscing elit, sed do eiusmod tempor incididunt ut labore</p>

  <div class="photo" style="left:608px;top:1102px;width:481px;height:218px;background:linear-gradient(135deg,#3a2a22 0%,#b0713e 50%,#d8b8a0 100%)" role="img" aria-label="Striped gift box of biscuits with green ribbon"></div>
  <div class="photo" style="left:608px;top:1340px;width:481px;height:218px;background:linear-gradient(135deg,#3d5a3c 0%,#c99562 55%,#b83a3a 100%)" role="img" aria-label="Festive boxes of bone biscuits among pine branches"></div>
</section>

<section>
  <div class="abs banner" role="img" aria-label="Dog lying among colourful bone biscuits"></div>
  <h2 class="abs banner-title">LOREM IPSUM DOLOR SIT AMET</h2>
  <a class="abs btn banner-btn" href="#">EXPLORE</a>
</section>

<section>
  <h2 class="abs section-title" style="top:2052px">NEW ARRIVALS</h2>
  <div class="abs product" style="left:111px"><div class="product-photo" style="background:radial-gradient(circle,#e6c9a0 0%,#8fb86a 40%,#fff 72%)" role="img" aria-label="Bone biscuits with a black gift box"></div><div class="product-name">Duis aute irure</div><div class="product-price">$24.00</div><a class="btn product-btn" href="#">ADD TO CART</a></div>
  <div class="abs product" style="left:359px"><div class="product-photo" style="background:radial-gradient(circle,#6a3a22 0%,#b08a66 50%,#fff 75%)" role="img" aria-label="Open box of dried chews"></div><div class="product-name">Duis aute irure</div><div class="product-price">$24.00</div><a class="btn product-btn" href="#">ADD TO CART</a></div>
  <div class="abs product" style="left:607px"><div class="product-photo" style="background:radial-gradient(circle,#a8602e 0%,#5a8ac8 40%,#fff 70%)" role="img" aria-label="Box of rolled chews"></div><div class="product-name">Duis aute irure</div><div class="product-price">$24.00</div><a class="btn product-btn" href="#">ADD TO CART</a></div>
  <div class="abs product" style="left:856px"><div class="product-photo" style="background:radial-gradient(circle,#d65a5a 0%,#9cc86a 35%,#2e2e2e 55%,#fff 75%)" role="img" aria-label="Black box of colourful bone biscuits"></div><div class="product-name">Duis aute irure</div><div class="product-price">$24.00</div><a class="btn product-btn" href="#">ADD TO CART</a></div>
</section>

<section>
  <h2 class="abs section-title" style="top:2535px">HOW IT WORK</h2>
  <div class="abs step" style="left:111px;background:linear-gradient(180deg,#b48a8e 0%,#c7a79a 60%,#d8d4d0 100%)" role="img" aria-label="Bowl of treats with a paw print">Nemo enim ipsam</div>
  <div class="abs step" style="left:443px;background:linear-gradient(135deg,#6e4a32 0%,#8a6a54 50%,#5c3c2a 100%)" role="img" aria-label="Assorted dog treats around a chalkboard sign">Nemo enim ipsam</div>
  <div class="abs step" style="left:775px;background:linear-gradient(180deg,#b8ab4a 0%,#c8b94e 60%,#a58a3a 100%)" role="img" aria-label="Dachshund standing on a parcel">Nemo enim ipsam</div>
</section>

<div class="abs promo">Save 20% when you buy three items with coupon BUYTHREE</div>

<footer class="abs footer">
  <div class="footer-col" style="left:111px;width:310px"><h3>About</h3><p>Lorem ipsum dolor sit amet, consectetur adipiscing elit, sed do eiusmod tempor incididunt ut labore et dolore magna aliqua. Ut enim ad minim veniam, quis nostrud</p></div>
  <div class="footer-col" style="left:446px"><h3>Our Collections</h3><ul><li>Search</li><li>About</li><li>Contact</li></ul></div>
  <div class="footer-col" style="left:643px"><h3>Explore</h3><ul><li>Reviews</li><li>Home</li><li>How it works</li><li>Blog</li><li>Info</li></ul></div>
  <div class="footer-col" style="left:806px"><h3>Connect</h3><p>Join our mailing list for updates</p></div>
  <div class="email">Email Id</div>
  <a class="btn join" href="#">JOIN</a>
  <div class="copyright">© Copyrights 2020 Company name | All Rights Reserved</div>
  <div class="payments"><span>PayLoop</span><span>Vantra</span><span>Cirquepay</span><span>Meridian</span></div>
</footer>

</body>
</html>
```